Clara Joy Halden- Lantern Waltz- Autumn/Winter Tour Dates

I need high res A3 Tour poster for print and for social media JPG sharing of tour dates.
Also needed Facebook/Twitter Banner Cover Photos of these dates.
Text Needed Below
Clara Joy Halden
Lantern Waltz
Autumn/Winter Tour Dates
03/09 Ravensby Folk Festival
21/09 Swindon- Calder Theatre
01/10 Hitchin- Brackwell Folk Club
17/10 Bath- The Anvil
20/10 Sheffield- Upper Dale Croquet Club
24/10 Birmingham- Orchard Lamp Cafe
26/10 Glasgow- The Nook and Jar
27/10 Edinburgh - The Marble Parlour
08/11 Capital Reel and Ballad Festival- The Crooked Heron
25/11 Lewes- Tandem Record Shop- Live In Store
02/12 Cambridge- The Quayside
27/01 Lincolnshire- Fenmarsh Theatre
Tickets/Info: www.clarajoyhalden-music.example/gigs
(Quotes/Reviews To Put On)
"Outstanding, rich and expressive."            "Vibrant and Experimental"
**** BdM                                                               **** Tunepaths
"Impressive and Invigorating"                        "Enchanting" Acoustic Wire UK
tBarks

Updates
I cannot read the tour dates on most of the submissions so far. They need to be visible to viewers.
Thank You.
Please also be as creative and inventive as possible- not bland.

Target Market(s)
Music Fans- Folk Acoustic Americana
Industry/Entity Type
Media
Font styles to use
Requirements
Must have
- My photo featured prominently
- Look classy and not tacky or OTT
- Look elegant, wintery and eye catching
- The dates must be very clear to read
- Links to Website:

Nice to have
- Something innovative and not boring in terms of layout design
- Perhaps fading/ misty or wintery

Should not have
- Any colours that do not match

```html
<!DOCTYPE html>
<html lang="en">
<head>
<meta charset="utf-8">
<title>Clara Joy Halden – Lantern Waltz – Autumn/Winter Tour</title>
<link rel="stylesheet" href="https://fonts.googleapis.com/css2?family=Cormorant+Garamond:ital,wght@0,400;0,500;1,600;1,700&family=Montserrat:wght@300;400;600;700;800&display=swap">
<style>
  :root {
    --night: #0b1123;
    --deep: #142445;
    --ice: #2c4f8a;
    --frost: #6f95c9;
    --snow: #ffffff;
    --mist: #d9e4f5;
    --serif: "Cormorant Garamond", Georgia, serif;
    --sans: "Montserrat", Arial, sans-serif;
  }
  * { margin: 0; padding: 0; box-sizing: border-box; }
  html, body { width: 849px; height: 1200px; overflow: hidden; background: var(--night); }
  .poster {
    position: relative;
    width: 849px;
    height: 1200px;
    overflow: hidden;
    color: var(--snow);
    font-family: var(--sans);
  }
  .artist-photo {
    position: absolute;
    inset: 0;
    width: 849px;
    height: 1200px;
    display: block;
  }
  .centered { position: absolute; left: 0; width: 100%; text-align: center; }

  .lead-review .quote {
    top: 62px;
    font-family: var(--serif);
    font-style: italic;
    font-weight: 700;
    font-size: 30px;
    letter-spacing: 1px;
  }
  .lead-review .stars { top: 104px; font-size: 20px; letter-spacing: 4px; }
  .lead-review .rule {
    position: absolute; top: 136px; left: 386px; width: 98px; height: 1px; background: var(--snow);
  }
  .lead-review .source { top: 145px; font-size: 12px; font-weight: 700; letter-spacing: 0.5px; }

  .artist-name {
    top: 216px;
    font-family: var(--serif);
    font-weight: 500;
    font-size: 32px;
    letter-spacing: 5px;
  }
  .album-title {
    top: 256px;
    font-weight: 700;
    font-size: 76px;
    letter-spacing: 1px;
    text-shadow: 0 0 18px rgba(210,190,255,0.5);
  }
  .tour-title {
    top: 718px;
    font-family: var(--serif);
    font-weight: 500;
    font-size: 34px;
    letter-spacing: 4px;
  }

  .reviews {
    position: absolute;
    left: 134px;
    top: 778px;
    width: 190px;
    text-align: center;
  }
  .review { margin-bottom: 18px; }
  .review .line { font-weight: 300; font-size: 15px; line-height: 16px; letter-spacing: 0.6px; }
  .review .stars { font-size: 8px; letter-spacing: 1px; margin-top: 2px; }
  .review .source { font-size: 9px; font-weight: 700; }

  .dates {
    position: absolute;
    left: 322px;
    top: 774px;
    list-style: none;
    font-size: 13.6px;
    letter-spacing: 0.4px;
  }
  .dates li { display: flex; line-height: 18.8px; }
  .dates .day { width: 55px; font-weight: 700; font-size: 11.5px; }
  .dates .city { font-weight: 700; margin-right: 5px; }
  .dates .venue { font-weight: 300; }

  .tickets-label { top: 1057px; font-weight: 600; font-size: 18px; letter-spacing: 3px; }
  .tickets-link { top: 1083px; font-weight: 600; font-size: 23px; letter-spacing: 3px; }
  .socials {
    position: absolute; top: 1127px; left: 0; width: 100%;
    display: flex; justify-content: center; gap: 22px;
    font-size: 12.5px; font-weight: 400;
  }
  .socials span { display: flex; align-items: center; gap: 5px; }
  .socials i { width: 10px; height: 10px; background: var(--snow); border-radius: 2px; display: inline-block; }
</style>
</head>
<body>
<main class="poster">
  <svg class="artist-photo" viewBox="0 0 849 1200" role="img" aria-label="Photo of the artist lying upside down in dark starry water, long dark hair spreading wide, strings of small lights around her">
    <defs>
      <linearGradient id="water" x1="0" y1="0" x2="0" y2="1">
        <stop offset="0" stop-color="#0e1528"/>
        <stop offset="0.3" stop-color="#1b2748"/>
        <stop offset="0.6" stop-color="#1c3463"/>
        <stop offset="0.8" stop-color="#27508c"/>
        <stop offset="1" stop-color="#2a4d86"/>
      </linearGradient>
      <radialGradient id="fabric" cx="0.5" cy="0.5" r="0.5">
        <stop offset="0" stop-color="#6a5a78" stop-opacity="0.75"/>
        <stop offset="1" stop-color="#3a3350" stop-opacity="0"/>
      </radialGradient>
      <radialGradient id="hair" cx="0.5" cy="0.5" r="0.5">
        <stop offset="0" stop-color="#05070f" stop-opacity="0.95"/>
        <stop offset="0.7" stop-color="#080c1a" stop-opacity="0.8"/>
        <stop offset="1" stop-color="#0a1022" stop-opacity="0"/>
      </radialGradient>
      <radialGradient id="skin" cx="0.5" cy="0.5" r="0.5">
        <stop offset="0" stop-color="#a9afc4" stop-opacity="0.85"/>
        <stop offset="0.6" stop-color="#6e7895" stop-opacity="0.6"/>
        <stop offset="1" stop-color="#3a4466" stop-opacity="0"/>
      </radialGradient>
      <radialGradient id="glow" cx="0.5" cy="0.5" r="0.5">
        <stop offset="0" stop-color="#6f95c9" stop-opacity="0.55"/>
        <stop offset="1" stop-color="#6f95c9" stop-opacity="0"/>
      </radialGradient>
    </defs>
    <rect width="849" height="1200" fill="url(#water)"/>
    <ellipse cx="430" cy="170" rx="300" ry="170" fill="url(#fabric)"/>
    <ellipse cx="470" cy="250" rx="110" ry="90" fill="url(#fabric)"/>
    <ellipse cx="425" cy="500" rx="420" ry="190" fill="url(#hair)"/>
    <ellipse cx="430" cy="420" rx="260" ry="120" fill="url(#hair)"/>
    <ellipse cx="425" cy="550" rx="125" ry="170" fill="url(#skin)"/>
    <ellipse cx="150" cy="680" rx="160" ry="110" fill="url(#glow)"/>
    <ellipse cx="700" cy="700" rx="170" ry="120" fill="url(#glow)"/>
    <rect y="820" width="849" height="380" fill="#2a4f8a" opacity="0.25"/>
  </svg>

  <section class="lead-review">
    <p class="centered quote">"Outstanding, rich and expressive"</p>
    <p class="centered stars">★★★★</p>
    <div class="rule"></div>
    <p class="centered source">BDM MAGAZINE</p>
  </section>

  <h2 class="centered artist-name">CLARA JOY HALDEN</h2>
  <h1 class="centered album-title">LANTERN WALTZ</h1>
  <h2 class="centered tour-title">THE AUTUMN/WINTER TOUR</h2>

  <aside class="reviews">
    <div class="review">
      <p class="line">"VIBRANT AND</p>
      <p class="line">EXPERIMENTAL"</p>
      <p class="stars">★★★★</p>
      <p class="source">TUNEPATHS</p>
    </div>
    <div class="review">
      <p class="line">"IMPRESSIVE AND</p>
      <p class="line">INVIGORATING"</p>
      <p class="source">tBarks</p>
    </div>
    <div class="review">
      <p class="line">"ENCHANTING"</p>
      <p class="source">ACOUSTIC WIRE UK</p>
    </div>
  </aside>

  <ul class="dates">
    <li><span class="day">03/09</span><span><span class="city">RAVENSBY</span><span class="venue">FOLK FESTIVAL</span></span></li>
    <li><span class="day">21/09</span><span><span class="city">SWINDON</span><span class="venue">CALDER THEATRE</span></span></li>
    <li><span class="day">01/10</span><span><span class="city">HITCHIN</span><span class="venue">BRACKWELL FOLK CLUB</span></span></li>
    <li><span class="day">17/10</span><span><span class="city">BATH</span><span class="venue">THE ANVIL</span></span></li>
    <li><span class="day">20/10</span><span><span class="city">SHEFFIELD</span><span class="venue">UPPER DALE CROQUET CLUB</span></span></li>
    <li><span class="day">24/10</span><span><span class="city">BIRMINGHAM</span><span class="venue">ORCHARD LAMP CAFE</span></span></li>
    <li><span class="day">26/10</span><span><span class="city">GLASGOW</span><span class="venue">THE NOOK AND JAR</span></span></li>
    <li><span class="day">27/10</span><span><span class="city">EDINBURGH</span><span class="venue">THE MARBLE PARLOUR</span></span></li>
    <li><span class="day">08/11</span><span><span class="city">CAPITAL REEL</span><span class="venue">AND BALLAD FESTIVAL</span><br><span class="venue">THE CROOKED HERON</span></span></li>
    <li><span class="day">25/11</span><span><span class="city">LEWES</span><span class="venue">TANDEM RECORD SHOP: LIVE IN STORE</span></span></li>
    <li><span class="day">02/12</span><span><span class="city">CAMBRIDGE</span><span class="venue">THE QUAYSIDE</span></span></li>
    <li><span class="day">27/01</span><span><span class="city">LINCOLNSHIRE</span><span class="venue">FENMARSH THEATRE</span></span></li>
  </ul>

  <p class="centered tickets-label">TICKETS/INFO</p>
  <p class="centered tickets-link">CLARAJOYHALDEN-MUSIC.EXAMPLE/GIGS</p>
  <div class="socials">
    <span><i></i>@CLARAJOYHALDEN</span>
    <span><i></i>/CLARAJOYHALDENMUSIC</span>
    <span><i></i>/CLARAJOYHALDEN</span>
  </div>
</main>
</body>
</html>
```